Creative Photography Business Card

Looking for a unique, creative, elegant, sophisticated and professional business card for my photography business.

I specialise in children, families, modelling, weddings and special event photography

Things to include:
Logo - will attach
Email: hello@mirabellwoodsphoto.com.au
web:www.mirabellwoodsphoto.com.au
Ph: 0438 502 671

I will also upload some of my work that you may like to use.

Please be creative and unique in your designs.

```html
<!DOCTYPE html>
<html lang="en">
<head>
<meta charset="utf-8">
<title>Mirabell Woods Photography – Business Card</title>
<link rel="stylesheet" href="https://fonts.googleapis.com/css2?family=Didact+Gothic&display=swap">
<style>
  :root {
    --page-bg: #ffffff;
    --card-shadow: rgba(0, 0, 0, 0.45);
    --photo-meadow: #dcdab4;
    --photo-light: #efe8c4;
    --photo-bark: #8d6a47;
    --photo-mid: #7a5436;
    --photo-shade: #5e3f27;
    --ink-soft: #5b4a3b;
    --ink-contact: #6a5646;
    --ink-mark: rgba(60, 38, 26, 0.78);
    --rule: rgba(70, 50, 35, 0.35);
  }
  * { margin: 0; padding: 0; box-sizing: border-box; }
  html, body {
    width: 1200px;
    height: 1000px;
    overflow: hidden;
    background: var(--page-bg);
  }
  .canvas {
    position: relative;
    width: 1200px;
    height: 1000px;
    font-family: "Didact Gothic", "Century Gothic", sans-serif;
  }
  .card {
    position: absolute;
    left: 232px;
    width: 723px;
    height: 414px;
    overflow: hidden;
    box-shadow: 5px 6px 7px var(--card-shadow);
  }
  .card--front { top: 58px; }
  .card--back { top: 546px; }
  .card__photo {
    position: absolute;
    inset: 0;
    background: linear-gradient(90deg,
      var(--photo-meadow) 0%,
      var(--photo-light) 30%,
      var(--photo-light) 36%,
      var(--photo-bark) 40%,
      var(--photo-mid) 70%,
      var(--photo-shade) 100%);
  }
  .brand-name {
    position: absolute;
    left: 0;
    right: 0;
    text-align: center;
    color: var(--ink-mark);
    line-height: 1.05;
  }
  .card--front .brand-name {
    top: 106px;
    font-size: 34px;
  }
  .brand-name__sub {
    display: block;
    font-size: 0.42em;
    letter-spacing: 0.3em;
    margin-top: 8px;
  }
  .card--back .brand-name {
    top: 140px;
    font-size: 60px;
  }
  .rule {
    position: absolute;
    left: 240px;
    width: 245px;
    height: 1px;
    background: linear-gradient(90deg, transparent, var(--rule), transparent);
  }
  .rule--top { top: 187px; }
  .rule--bottom { top: 252px; }
  .tagline {
    position: absolute;
    top: 210px;
    left: 0;
    right: 0;
    text-align: center;
    font-size: 17.5px;
    color: var(--ink-soft);
    letter-spacing: 0.01em;
  }
  .contact {
    position: absolute;
    top: 308px;
    left: 0;
    right: 0;
    text-align: center;
    list-style: none;
    font-size: 14px;
    line-height: 21px;
    color: var(--ink-contact);
  }
</style>
</head>
<body>
<main class="canvas">
  <section class="card card--front">
    <div class="card__photo" role="img" aria-label="Softly blurred outdoor portrait of a child in an orange top against a tree trunk and sunlit meadow"></div>
    <p class="brand-name">Mirabell Woods<span class="brand-name__sub">PHOTOGRAPHY</span></p>
    <div class="rule rule--top"></div>
    <p class="tagline">Children, families, modelling, weddings and special event photography</p>
    <div class="rule rule--bottom"></div>
    <ul class="contact">
      <li>hello@mirabellwoodsphoto.com.au</li>
      <li>www.mirabellwoodsphoto.com.au</li>
      <li>0438 502 671</li>
    </ul>
  </section>

  <section class="card card--back">
    <div class="card__photo" role="img" aria-label="Softly blurred outdoor portrait of a child in an orange top against a tree trunk and sunlit meadow"></div>
    <p class="brand-name">Mirabell Woods<span class="brand-name__sub">PHOTOGRAPHY</span></p>
  </section>
</main>
</body>
</html>
```